Breezeway Comfort business cards design

Need a business card design for a Heating and Air Conditioning business. I need these items included.
Business name: Breezeway Comfort
Owner: Marcus Tollefsen
License # 2874590
Phone number # 555-382-4071
Email: breezewaycomfortair@mailvista.example
Sales
Service
Installation
Maintenance

Heating and Air Conditioning

Requirements
Must have
• Company name , license number , phone number , email

```html
<!DOCTYPE html>
<html lang="en">
<head>
<meta charset="UTF-8">
<title>Breezeway Comfort — Business Cards</title>
<link href="https://fonts.googleapis.com/css2?family=Poppins:wght@400;600;700&display=swap" rel="stylesheet">
<style>
  :root {
    --page-bg: #ececec;
    --card-bg: #ffffff;
    --brand-blue: #1e44a6;
    --ink: #1f2a44;
    --accent-orange: #f26a4b;
    --rule-peach: #f7b3a2;
  }
  * { margin: 0; padding: 0; box-sizing: border-box; }
  html, body {
    width: 1199px;
    height: 1200px;
    overflow: hidden;
    background: var(--page-bg);
    font-family: "Poppins", sans-serif;
  }
  .card {
    position: absolute;
    left: 150px;
    width: 897px;
    height: 526px;
    background: var(--card-bg);
  }
  .card--front { top: 59px; }
  .card--back { top: 624px; }

  .brand-mark {
    position: absolute;
    display: flex;
    align-items: center;
    gap: 22px;
    color: var(--brand-blue);
    font-weight: 700;
    text-transform: uppercase;
    letter-spacing: 1px;
  }
  .brand-mark__dot {
    border-radius: 50%;
    background: var(--accent-orange);
    flex: none;
  }
  .card--front .brand-mark {
    left: 62px;
    top: 95px;
    font-size: 50px;
    line-height: 1.05;
  }
  .card--front .brand-mark__dot { width: 120px; height: 120px; }

  .card--back .brand-mark {
    left: 0;
    right: 0;
    top: 120px;
    flex-direction: column;
    gap: 30px;
    text-align: center;
    font-size: 58px;
    line-height: 1.05;
  }
  .card--back .brand-mark__dot { width: 130px; height: 130px; }

  .owner {
    position: absolute;
    left: 63px;
    top: 289px;
  }
  .owner__name {
    font-size: 36px;
    font-weight: 600;
    color: var(--brand-blue);
    line-height: 1.2;
  }
  .owner__role {
    font-size: 21px;
    font-weight: 400;
    color: var(--brand-blue);
    line-height: 1.2;
  }

  .contact {
    position: absolute;
    left: 63px;
    top: 395px;
    list-style: none;
  }
  .contact__item {
    display: flex;
    align-items: center;
    gap: 15px;
    font-size: 21px;
    color: var(--ink);
    height: 41px;
  }
  .contact__icon { width: 20px; height: 20px; flex: none; }

  .license {
    position: absolute;
    right: 81px;
    top: 419px;
    width: 194px;
    border-top: 2px solid var(--rule-peach);
    padding-top: 12px;
    text-align: right;
    font-size: 21px;
    color: var(--ink);
    white-space: nowrap;
  }
</style>
</head>
<body>

<section class="card card--front">
  <div class="brand-mark">
    <span class="brand-mark__dot"></span>
    <span class="brand-mark__name">Breezeway<br>Comfort</span>
  </div>

  <div class="owner">
    <p class="owner__name">Marcus Tollefsen</p>
    <p class="owner__role">Owner</p>
  </div>

  <ul class="contact">
    <li class="contact__item">
      <svg class="contact__icon" viewBox="0 0 24 24" aria-hidden="true">
        <path fill="var(--accent-orange)" d="M6.6 10.8a15.1 15.1 0 0 0 6.6 6.6l2.2-2.2a1 1 0 0 1 1-.25 11.4 11.4 0 0 0 3.6.57 1 1 0 0 1 1 1V20a1 1 0 0 1-1 1A17 17 0 0 1 3 4a1 1 0 0 1 1-1h3.5a1 1 0 0 1 1 1c0 1.25.2 2.45.57 3.57a1 1 0 0 1-.25 1z"/>
      </svg>
      <span>555-382-4071</span>
    </li>
    <li class="contact__item">
      <svg class="contact__icon" viewBox="0 0 24 24" aria-hidden="true">
        <rect x="2" y="5" width="20" height="14" rx="2" fill="var(--accent-orange)"/>
        <path d="M3 7l9 6 9-6" fill="none" stroke="#fff" stroke-width="1.8"/>
      </svg>
      <span>breezewaycomfortair@mailvista.example</span>
    </li>
  </ul>

  <p class="license">License # 2874590</p>
</section>

<section class="card card--back">
  <div class="brand-mark">
    <span class="brand-mark__dot"></span>
    <span class="brand-mark__name">Breezeway<br>Comfort</span>
  </div>
</section>

</body>
</html>
```